Capability Statement Flyer

We want to develop a flyer to show potential clients our work capability. We want to incorporate our logo. You can reference our website for any other graphics you may want to incorporate. Our blue CMYK is 100-80-0-22

Colors
0555a3

Requirements
Must have
• Capability Statement
• Our expertise and technical resources fuel the delivery of our services. As a leading provider of construction services, Halvern Construction focuses on providing solutions for civil infrastructure, industrial infrastructure, and commercial market segments. Driven by a commitment to continuous improvement, Halvern Construction has the expertise in the following key areas:
• • Design Build/Problem Solving
• • Storm and Process Water Systems
• • Heavy and Structural Concrete
• • Bridge Construction
• • Building Construction and Restoration
• • Hardscapes
• • All Civil Construction and Utility
Nice to have
• Creativity to present to potential clients. Not just words on the page

```html
<!DOCTYPE html>
<html lang="en">
<head>
<meta charset="utf-8">
<title>Halvern Construction – Capability Statement</title>
<link href="https://fonts.googleapis.com/css2?family=Oswald:wght@400;500&family=Open+Sans:wght@400;600&display=swap" rel="stylesheet">
<style>
:root{
  --navy:#263b82;
  --ink:#1a1a1a;
  --muted:#555a66;
  --stage:#a7a9ac;
  --paper:#ffffff;
  --paper-soft:#f3f4f8;
}
*{box-sizing:border-box;margin:0;padding:0}
html,body{width:992px;height:1200px;overflow:hidden;background:var(--stage)}
body{position:relative;font-family:"Open Sans",sans-serif;color:var(--ink)}
.page{position:absolute;width:413px;height:533px;background:linear-gradient(90deg,var(--paper),var(--paper-soft));box-shadow:3px 4px 8px rgba(0,0,0,.25);overflow:hidden}
.cover{left:71px;top:68px;background:var(--navy);color:#fff}
.title-page{left:505px;top:68px}
.expertise-page{left:67px;top:629px}
.services-page{left:505px;top:629px}
.abs{position:absolute}
.cond{font-family:"Oswald",sans-serif;font-weight:500}
.photo{position:absolute}
.site{position:absolute;left:0;width:100%;text-align:center;font-size:11.5px;display:flex;justify-content:center;align-items:center;gap:10px}
.site::before,.site::after{content:"";width:55px;height:1px;background:currentColor;opacity:.6}
.wordmark{position:absolute;display:flex;align-items:center;gap:9px;font-family:"Oswald",sans-serif;font-weight:500}
.wordmark .mark{background:currentColor}
.wordmark .name{line-height:.95;text-transform:uppercase}
.cover .wordmark{left:79px;top:282px;color:#fff}
.cover .mark{width:54px;height:54px}
.cover .name{font-size:40px}
.cover .name small{display:block;font-size:20px;letter-spacing:1px}
.contact{position:absolute;left:79px;top:376px;font-size:9.5px;line-height:13px}
.contact .gap{height:9px}
.contact svg{width:8px;height:8px;vertical-align:-1px;margin-right:5px;fill:#fff}
.bands .band{position:absolute;top:51px;height:21px}
.title-page .wordmark{left:63px;top:254px;color:var(--navy)}
.title-page .mark{width:66px;height:66px}
.title-page .name{font-size:52px}
.title-page .name small{display:block;font-size:24px;letter-spacing:1px}
.doc-title{position:absolute;left:0;width:100%;top:382px;text-align:center;font-family:"Oswald",sans-serif;font-weight:500;font-size:38px;color:var(--ink)}
.doc-title span{color:var(--navy)}
.sidebar{position:absolute;left:0;top:23px;width:115px;height:452px;background:var(--navy);color:#fff}
.sidebar h3{font-family:"Oswald",sans-serif;font-weight:400;font-size:13px;position:absolute;left:14px}
.sidebar p{position:absolute;left:14px;width:94px;font-size:6.6px;line-height:10px}
.key-heading{position:absolute;left:138px;top:38px;font-family:"Oswald",sans-serif;font-weight:400;font-size:16px;line-height:23px;color:var(--navy)}
.key-list{position:absolute;left:146px;top:102px;list-style:none;font-size:10.5px;color:#444}
.key-list li{height:18.3px;display:flex;align-items:center;gap:14px}
.key-list li::before{content:"";width:10px;height:10px;background:var(--navy)}
.help-heading{position:absolute;left:141px;top:277px;font-family:"Oswald",sans-serif;font-weight:400;font-size:13px;color:var(--navy)}
.step{position:absolute;left:140px;width:240px;height:50px}
.step .icon{position:absolute;left:8px;top:0;width:32px;height:32px;border-radius:50%;background:#e4e5ea;display:flex;align-items:center;justify-content:center}
.step .icon svg{width:15px;height:15px;fill:var(--navy)}
.step .tag{position:absolute;left:2px;top:26px;width:42px;background:#111;color:#fff;border-radius:6px;font-size:7.5px;font-weight:600;text-align:center;line-height:11px}
.step p{position:absolute;left:66px;top:0;width:165px;font-size:6.3px;line-height:9px;color:#333}
.review{position:absolute;left:386px;top:0;width:162px;height:171px;background:var(--navy);color:#fff}
.review{left:386px}
.review h3{position:absolute;left:12px;top:20px;font-family:"Oswald",sans-serif;font-weight:400;font-size:15px}
.review .q{position:absolute;font-family:Georgia,serif;font-size:20px;font-weight:bold;line-height:1}
.review p{position:absolute;left:33px;top:52px;width:122px;font-size:6.3px;line-height:9.2px}
.story-head{position:absolute;left:29px;top:240px;font-family:"Oswald",sans-serif;font-weight:400;font-size:15px;line-height:21px;color:var(--navy)}
.story-sub{position:absolute;left:29px;top:294px;font-family:"Oswald",sans-serif;font-weight:400;font-size:10.5px;line-height:15px}
.story-body{position:absolute;left:29px;top:328px;width:196px;font-size:6.3px;line-height:9.2px;color:#333}
.services-heading{position:absolute;left:243px;top:189px;font-family:"Oswald",sans-serif;font-weight:400;font-size:15px}
.service{position:absolute;left:243px;width:150px;height:45px}
.service svg{position:absolute;left:0;top:4px;width:22px;height:22px;fill:var(--navy)}
.service h4{position:absolute;left:35px;top:0;font-family:"Oswald",sans-serif;font-weight:400;font-size:11.5px;color:var(--navy)}
.service p{position:absolute;left:35px;top:16px;width:115px;font-size:6.2px;line-height:9.5px;color:#333}
</style>
</head>
<body>

<section class="page cover">
  <div class="wordmark"><span class="mark"></span><span class="name">Halvern<small>Construction</small></span></div>
  <div class="contact">
    <div>Address:</div>
    <div>0000 Birchwood Ave #000</div>
    <div>Carrow Falls</div>
    <div class="gap"></div>
    <div><svg viewBox="0 0 10 10"><path d="M2 0h2l1 3-1.5 1a6 6 0 0 0 2.5 2.5L7 5l3 1v2a2 2 0 0 1-2 2A8 8 0 0 1 0 2a2 2 0 0 1 2-2z"/></svg>(555) 010-0000</div>
    <div><svg viewBox="0 0 10 10"><rect x="2" y="0" width="6" height="10" rx="1"/></svg>(555) 010-0001</div>
    <div><svg viewBox="0 0 10 10"><rect x="0" y="2" width="10" height="6" rx="1"/></svg>info@halvernconstruction.com</div>
  </div>
  <div class="site" style="top:491px">www.halvernconstruction.com</div>
</section>

<section class="page title-page">
  <div class="bands">
    <div class="band" style="left:0;width:130px;background:var(--navy)"></div>
    <div class="band" style="left:142px;width:129px;background:#000"></div>
    <div class="band" style="left:283px;width:130px;background:var(--navy)"></div>
  </div>
  <div class="photo" role="img" aria-label="House frame under construction at sunset" style="left:0;top:84px;width:130px;height:95px;background:linear-gradient(160deg,#c9965a,#6e5a44 55%,#4f6b3a)"></div>
  <div class="photo" role="img" aria-label="Aerial view of highway interchange" style="left:142px;top:84px;width:129px;height:95px;background:linear-gradient(135deg,#3d5660,#6f8a8f 50%,#36504a)"></div>
  <div class="photo" role="img" aria-label="Workers on a construction site seen from above" style="left:283px;top:84px;width:130px;height:95px;background:linear-gradient(160deg,#8a6a4e,#5b4634 60%,#7d6a58)"></div>
  <div class="wordmark"><span class="mark"></span><span class="name">Halvern<small>Construction</small></span></div>
  <h1 class="doc-title"><span>CAPABILITY</span> STATEMENT</h1>
  <div class="site" style="top:490px">www.halvernconstruction.com</div>
</section>

<section class="page expertise-page">
  <aside class="sidebar">
    <div class="photo" role="img" aria-label="House under construction" style="left:0;top:15px;width:115px;height:83px;background:linear-gradient(160deg,#b88a58,#7a6452 50%,#566d3e)"></div>
    <h3 style="top:115px">WELCOME</h3>
    <p style="top:139px">Our expertise and technical resources fuel the delivery of our services. As a leading provider of construction services, Halvern Construction focuses on providing solutions for civil infrastructure, industrial infrastructure, and commercial market segments. Driven by a commitment to continuous improvement.</p>
    <h3 style="top:300px">MISSION</h3>
    <p style="top:322px">Lorem ipsum dolor sit amet, consectetur adipiscing elit, sed do eiusmod tempor incididunt ut labore et dolore magna aliqua. Ut enim ad minim veniam, quis nostrud exercitation ullamco laboris nisi ut aliquip ex ea commodo consequat.</p>
  </aside>
  <h2 class="key-heading">Halvern Construction has the expertise<br>in the following key areas:</h2>
  <ul class="key-list">
    <li>Design Build/Problem Solving</li>
    <li>Storm and Process Water Systems</li>
    <li>Heavy and Structural Concrete</li>
    <li>Bridge Construction</li>
    <li>Building Construction and Restoration</li>
    <li>Hardscapes</li>
    <li>All Civil Construction and Utility</li>
  </ul>
  <h3 class="help-heading">HOW WE CAN HELP YOU</h3>
  <div class="step" style="top:305px">
    <span class="icon"><svg viewBox="0 0 10 10"><path d="M2 0h5l2 2v8H2z M3.5 4h4v.8h-4z M3.5 6h4v.8h-4z" fill-rule="evenodd"/></svg></span>
    <span class="tag">STEP 1</span>
    <p>Lorem ipsum dolor sit amet, consectetur adipiscing elit, sed do eiusmod tempor incididunt ut labore et dolore magna aliqua. Ut enim ad minim veniam, quis nostrud exercitation ullamco laboris nisi ut aliquip ex ea commodo consequat. Duis aute irure dolor in</p>
  </div>
  <div class="step" style="top:360px">
    <span class="icon"><svg viewBox="0 0 10 10"><path d="M2 0h6v10H2z M3 1h4v2H3z M3 4.5h1v1H3z M4.5 4.5h1v1h-1z M6 4.5h1v1H6z M3 6.5h1v1H3z M4.5 6.5h1v1h-1z M6 6.5h1v1H6z" fill-rule="evenodd"/></svg></span>
    <span class="tag">STEP 2</span>
    <p>Lorem ipsum dolor sit amet, consectetur adipiscing elit, sed do eiusmod tempor incididunt ut labore et dolore magna aliqua. Ut enim ad minim veniam, quis nostrud exercitation ullamco laboris nisi ut aliquip ex ea commodo consequat. Duis aute irure dolor in</p>
  </div>
  <div class="step" style="top:415px">
    <span class="icon"><svg viewBox="0 0 10 10"><path d="M5 0l5 4.5H8.5V10h-7V4.5H0z"/></svg></span>
    <span class="tag">STEP 3</span>
    <p>Lorem ipsum dolor sit amet, consectetur adipiscing elit, sed do eiusmod tempor incididunt ut labore et dolore magna aliqua. Ut enim ad minim veniam, quis nostrud exercitation ullamco laboris nisi ut aliquip ex ea commodo consequat. Duis aute irure dolor in</p>
  </div>
  <div class="site" style="top:504px">www.halvernconstruction.com</div>
</section>

<section class="page services-page">
  <div class="photo" role="img" aria-label="Worker in hard hat climbing scaffolding" style="left:29px;top:22px;width:193px;height:196px;background:linear-gradient(160deg,#7b6b5c,#a78c6c 50%,#5e5046)"></div>
  <div class="review" style="left:237px">
    <h3>OUR CLIENT REVIEW</h3>
    <span class="q" style="left:12px;top:52px">“</span>
    <p>Lorem ipsum dolor sit amet, consectetur adipiscing elit, sed do eiusmod tempor incididunt ut labore et dolore magna aliqua. Ut enim ad minim veniam, quis nostrud exercitation ullamco laboris nisi ut aliquip ex ea commodo consequat. Duis aute irure dolor in reprehenderit in voluptate velit esse cillum dolore eu fugiat nulla pariatur. Excepteur sint occaecat cupidatat non proident, sunt in culpa qui officia deserunt mollit anim laborum.</p>
    <span class="q" style="left:136px;top:148px">”</span>
  </div>
  <h2 class="story-head">LOREM IPSUM DOLOR SIT<br>AMET, DUNT UT LABORE ET</h2>
  <h3 class="story-sub">LOREM IPSUM DOLOR SIT AMET,<br>CONSECTETUR ADIPISCING</h3>
  <p class="story-body">"Lorem ipsum dolor sit amet, consectetur adipiscing elit, sed do eiusmod tempor incididunt ut labore et dolore magna aliqua. Ut enim ad minim veniam, quis nostrud exercitation ullamco laboris nisi ut aliquip ex ea commodo consequat. Duis aute irure dolor in reprehenderit in voluptate velit esse cillum dolore eu fugiat nulla pariatur. Excepteur sint occaecat cupidatat non proident, sunt in culpa qui officia deserunt mollit anim id est laborum."Lorem ipsum dolor sit amet, consectetur adipiscing elit, sed do eiusmod tempor incididunt ut labore et dolore magna aliqua. Ut enim ad minim veniam, quis nostrud exercitation ullamco laboris nisi ut aliquip ex ea commodo consequat. Duis aute irure dolor in reprehenderit in voluptate velit esse cillum dolore eu fugiat nulla pariatur. Excepteur sint occaecat cupidatat non proident, sunt in culpa qui officia deserunt mollit anim id est laborum.</p>
  <h3 class="services-heading">SERVICES WE OFFER</h3>
  <div class="service" style="top:226px">
    <svg viewBox="0 0 10 10"><path d="M3.5 0h3L6 2H4z M5 2.5a4 4 0 0 1 4 4.5 3 3 0 0 1-3 3H4a3 3 0 0 1-3-3 4 4 0 0 1 4-4.5z"/></svg>
    <h4>FINANCIAL</h4>
    <p>Lorem ipsum dolor sit amet, consectetur adipiscing elit, sed do eiusmod tempor incididunt.</p>
  </div>
  <div class="service" style="top:276px">
    <svg viewBox="0 0 10 10"><path d="M0 1h7v1H1v7h7V6h1v4H0z M8 1l1.5 1.5L5 7H3.5V5.5z"/></svg>
    <h4>WRITTEN DOCUMENTS</h4>
    <p>Lorem ipsum dolor sit amet, consectetur adipiscing elit, sed do eiusmod tempor incididunt .</p>
  </div>
  <div class="service" style="top:326px">
    <svg viewBox="0 0 10 10"><path d="M1 0h5l2 2v3H7V3H5V1H2v8h3v1H1z"/><circle cx="8" cy="8" r="2"/></svg>
    <h4>LOAN APPROVAL</h4>
    <p>Lorem ipsum dolor sit amet, consectetur adipiscing elit, sed do eiusmod tempor incididunt.</p>
  </div>
  <div class="service" style="top:376px">
    <svg viewBox="0 0 10 10"><path d="M0 1.5h9v3H8V4H1v5h4v1H0z M2 0h1v2H2z M6 0h1v2H6z"/><circle cx="8" cy="8" r="2"/></svg>
    <h4>SCHEDULE MANAGEMENT</h4>
    <p>Lorem ipsum dolor sit amet, consectetur adipiscing elit, sed do eiusmod tempor incididunt.</p>
  </div>
  <div class="service" style="top:426px">
    <svg viewBox="0 0 10 10"><path d="M5 0.5a4.5 4.5 0 1 1-4.2 6l1-.4A3.4 3.4 0 1 0 5 1.6V3L2.8 1 5 -1z M4.5 3h1v4h-1z"/></svg>
    <h4>FUNDING</h4>
    <p>Lorem ipsum dolor sit amet, consectetur adipiscing elit, sed do eiusmod tempor incididunt.</p>
  </div>
  <div class="site" style="top:503px">www.halvernconstruction.com</div>
</section>

</body>
</html>
```